Allied Health team of Physiotherapists & Occupational Therapists seek a business card design

We have our new logo, we now need our new business cards and stationary. Blossom: Lymphoedema & Women's Clinic is seeking a generic card design to represent our whole team and individual cards for each therapist that incorporates our new logo to communicate our holistic approach that is calming, nuturing, supportive and welcoming.
Our Physiotherapists and Occupational Therapists assess, treat and provide education for people who are at risk of or who have lymphoedema. This is often as a result of treatment for cancer. We provide pre-operative and post-operative management and cancer rehabilitation in our Pilates studio. Our team also consists of Physiotherapists who have a strong interest in pelvic floor and continence management for both men and women.

Target Market(s)

Mainly women health conscious

Industry/Entity Type

Allied Health: Physiotherapy / Occupational Therapy

Contact Information for Business Card

Address: 14 Calloway Ave Larkfield 3941 Phone: 84317560 fax: 8431 7564 Email: info@blossomcarepartners.com.au Website: blossomcarepartners.com.au Facebook address: facebook.com/BlossomLymphoedemaAndWomensCareCentre. Room to write appointments. Individual cards need to have name, office email and individual email and professional details

Requirements
Must have
• Logo as per uploaded documents

```html
<!DOCTYPE html>
<html lang="en">
<head>
<meta charset="utf-8">
<title>Blossom: Lymphoedema &amp; Women's Clinic – Business Card</title>
<link rel="stylesheet" href="https://fonts.googleapis.com/css2?family=Montserrat:wght@400;500;700&display=swap">
<style>
  :root {
    --page: #ececee;
    --card-white: #ffffff;
    --indigo: #2f2c96;
    --indigo-deep: #25237c;
    --peach: #f3a77a;
    --ink: #1c1c2a;
    --ink-soft: #4a4a5c;
  }
  * { margin: 0; padding: 0; box-sizing: border-box; }
  html, body {
    width: 1200px; height: 1200px; overflow: hidden;
    background: var(--page);
    font-family: "Montserrat", Arial, sans-serif;
  }
  .sheet {
    position: relative; width: 1200px; height: 1200px;
    display: flex; flex-direction: column; align-items: center; justify-content: center; gap: 60px;
  }
  .card {
    position: relative; width: 880px; height: 500px; overflow: hidden;
    border-radius: 6px; box-shadow: 0 10px 30px rgba(30, 30, 60, .15);
  }
  .card svg.card-shapes { position: absolute; inset: 0; width: 100%; height: 100%; }

  /* back */
  .card-back { background: var(--indigo); }
  .brand-seal {
    position: absolute; display: flex; align-items: center; justify-content: center;
    border-radius: 50%; border: 2px solid var(--peach);
    color: var(--peach); font-weight: 500; letter-spacing: .5px;
  }
  .card-back .brand-seal { width: 150px; height: 150px; left: 365px; top: 70px; font-size: 24px; }
  .back-band {
    position: absolute; left: 0; right: 0; top: 300px; height: 80px;
    background: var(--indigo-deep);
    display: flex; align-items: center; justify-content: center; gap: 12px;
    color: var(--peach); font-size: 22px; font-weight: 500; letter-spacing: .5px;
  }
  .band-dot { width: 22px; height: 22px; border-radius: 50%; background: var(--peach); }

  /* front */
  .card-front { background: var(--card-white); }
  .card-front .brand-seal { width: 170px; height: 170px; left: 70px; top: 275px; font-size: 26px; }
  .identity { position: absolute; right: 170px; top: 58px; text-align: right; }
  .person-name { font-size: 34px; font-weight: 700; color: var(--ink); }
  .credentials { margin-top: 8px; font-size: 12.5px; line-height: 1.5; color: var(--ink-soft); }
  .contact-list {
    position: absolute; left: 420px; top: 250px;
    display: grid; grid-template-columns: auto auto; column-gap: 40px; row-gap: 14px;
    font-size: 15px; color: var(--ink);
  }
  .contact-item { display: flex; align-items: center; gap: 10px; }
  .contact-item.wide { grid-column: 1 / span 2; }
  .icon {
    width: 24px; height: 24px; border-radius: 50%; background: var(--indigo);
    display: flex; align-items: center; justify-content: center; flex: none;
  }
  .icon svg { width: 14px; height: 14px; }
</style>
</head>
<body>
<main class="sheet">

  <section class="card card-back" aria-label="Business card back">
    <div class="brand-seal">Blossom</div>
    <div class="back-band"><span class="band-dot"></span>blossomcarepartners.com.au</div>
  </section>

  <section class="card card-front" aria-label="Business card front">
    <svg class="card-shapes" viewBox="0 0 880 500" aria-hidden="true">
      <circle cx="90" cy="450" r="318" fill="var(--peach)"/>
      <circle cx="90" cy="450" r="304" fill="var(--indigo)"/>
      <circle cx="990" cy="120" r="214" fill="var(--peach)"/>
      <circle cx="990" cy="120" r="200" fill="var(--indigo)"/>
    </svg>
    <div class="brand-seal">Blossom</div>

    <div class="identity">
      <h1 class="person-name">Maren Holloway</h1>
      <p class="credentials">
        B. Physiotherapy (Hons), Cert. Lymphoedema Practice<br>
        Women's Health &amp; Continence Physiotherapist<br>
        Pilates Studio Lead, Pre &amp; Post Operative Care
      </p>
    </div>

    <div class="contact-list">
      <div class="contact-item">
        <span class="icon"><svg viewBox="0 0 24 24"><path fill="#fff" d="M6.6 10.8a15 15 0 0 0 6.6 6.6l2.2-2.2c.3-.3.7-.4 1-.2 1.1.4 2.3.6 3.6.6.6 0 1 .4 1 1V20c0 .6-.4 1-1 1A17 17 0 0 1 3 4c0-.6.4-1 1-1h3.5c.6 0 1 .4 1 1 0 1.3.2 2.5.6 3.6.1.3 0 .7-.2 1z"/></svg></span>
        84317560
      </div>
      <div class="contact-item">
        <span class="icon"><svg viewBox="0 0 24 24"><path fill="#fff" d="M6 3h12v5H6zM4 9h16a2 2 0 0 1 2 2v6h-4v4H6v-4H2v-6a2 2 0 0 1 2-2zm4 7v3h8v-3z"/></svg></span>
        8431 7564
      </div>
      <div class="contact-item wide">
        <span class="icon"><svg viewBox="0 0 24 24"><path fill="#fff" d="M3 5h18v14H3zm2 2v.5l7 4.5 7-4.5V7z"/></svg></span>
        info@blossomcarepartners.com.au
      </div>
      <div class="contact-item wide">
        <span class="icon"><svg viewBox="0 0 24 24"><path fill="#fff" d="M12 2a7 7 0 0 0-7 7c0 5 7 13 7 13s7-8 7-13a7 7 0 0 0-7-7zm0 9.5A2.5 2.5 0 1 1 12 6.5a2.5 2.5 0 0 1 0 5z"/></svg></span>
        14 Calloway Ave, Larkfield 3941
      </div>
    </div>
  </section>

</main>
</body>
</html>
```